Cafe Menu for Maplebrook Lantern Cafe

Menu designed for my cafe. I need multiple sizes to be created.
DL pamphlet
A4
and I also need 5 x A3 portraits & 5 x A3 landscapes. The menu must be spread out over a total of 10 A3 pages. I have uploaded my logo which needs to be used & I would like the colours from the logo used. The background of the menu needs to be white. I have uploaded an image on another menu for which I would like the same heading font to be used.

Target Market(s)

cafe, restaurant

Font styles to use
Serif
Decorative
Script

Requirements
Must have
• White back ground
correct font as I have uploaded
Nice to have
• May have drawings of food in back and white.

```html
<!DOCTYPE html>
<html lang="en">
<head>
<meta charset="utf-8">
<title>Maplebrook Lantern Cafe – Breakfast &amp; Lunch Menu</title>
<link rel="stylesheet" href="https://fonts.googleapis.com/css2?family=Great+Vibes&family=Zilla+Slab:wght@600;700&family=Lato:wght@400&display=swap">
<style>
:root{
  --paper:#ffffff;
  --wash:#eef3ea;
  --ink:#2d2a26;
  --title:#3a3530;
  --desc:#b0703a;
  --brush:#e7a15a;
  --green:#9dbb8a;
  --brown:#6b4a32;
  --orange:#f2a93b;
  --cream:#f6ecd8;
}
*{margin:0;padding:0;box-sizing:border-box}
html,body{width:849px;height:1200px;overflow:hidden;background:var(--paper)}
.menu{position:relative;width:849px;height:1200px;overflow:hidden;
  background:radial-gradient(ellipse at 50% 45%,var(--paper) 55%,var(--wash) 100%)}
.art{position:absolute}
.section-title{position:absolute;left:0;width:100%;text-align:center;
  font-family:"Great Vibes",cursive;font-size:64px;color:var(--title);line-height:1}
.brush{position:absolute;border-radius:40px;opacity:.55;
  background:linear-gradient(90deg,transparent,var(--brush) 20%,var(--brush) 80%,transparent)}
.item{position:absolute;width:295px}
.item-head{display:flex;justify-content:space-between;align-items:baseline;
  font-family:"Zilla Slab",serif;font-weight:700;font-size:15.5px;color:var(--ink);line-height:1.15}
.item-head .name{max-width:210px}
.item-desc{font-family:"Lato",sans-serif;font-size:10px;line-height:1.3;color:var(--desc);margin-top:3px;max-width:230px}
</style>
</head>
<body>
<main class="menu">

  <div class="art" role="img" aria-label="Watercolour coffee beans and leaves" style="left:-20px;top:-20px;width:170px;height:140px;border-radius:50%;background:radial-gradient(circle,#7a5236 0%,#a88466 55%,transparent 75%)"></div>
  <div class="art" role="img" aria-label="Watercolour sliced avocado" style="left:-30px;top:175px;width:95px;height:110px;border-radius:50%;background:radial-gradient(circle,#d8dd8c 0%,#8fae5c 55%,transparent 75%)"></div>
  <div class="art" role="img" aria-label="Watercolour herbs and pencil sketch" style="left:690px;top:-20px;width:180px;height:150px;border-radius:50%;background:radial-gradient(circle,#c9d9b8 0%,#e9c7a3 55%,transparent 75%)"></div>
  <div class="art" role="img" aria-label="Watercolour green leaves" style="left:755px;top:430px;width:110px;height:140px;border-radius:50%;background:radial-gradient(circle,#a7c48e 0%,#cfe0c0 55%,transparent 75%)"></div>
  <div class="art" role="img" aria-label="Watercolour orange slice" style="left:770px;top:700px;width:110px;height:150px;border-radius:50%;background:radial-gradient(circle,var(--orange) 0%,#f7cf8a 55%,transparent 75%)"></div>
  <div class="art" role="img" aria-label="Watercolour fried eggs in a pan" style="left:660px;top:1010px;width:230px;height:220px;border-radius:50%;background:radial-gradient(circle,#fff6e0 0%,#f3c86a 30%,#d9d6cf 58%,transparent 75%)"></div>
  <div class="art" role="img" aria-label="Watercolour leaves and spices" style="left:-40px;top:990px;width:150px;height:230px;border-radius:50%;background:radial-gradient(circle,#b9cfa4 0%,#e3d7c0 55%,transparent 75%)"></div>

  <div class="brush" style="left:250px;top:70px;width:360px;height:30px"></div>
  <h1 class="section-title" style="top:22px">Breakfast Menu</h1>

  <div class="item" style="left:75px;top:140px"><div class="item-head"><span class="name">Big Breakfast</span><span>$21.50</span></div><p class="item-desc">Bacon, sausages, hash browns, tomato, baked beans &amp; mushrooms with a slice of toasted pane bread &amp; your choice of fried, poached or scrambled eggs</p></div>
  <div class="item" style="left:75px;top:225px"><div class="item-head"><span class="name">Avocado Stack</span><span>$17.00</span></div><p class="item-desc">Turkish bread topped with avocado, bacon or salmon, 2 poached eggs &amp; a sprinkle of feta cheese</p></div>
  <div class="item" style="left:75px;top:290px"><div class="item-head"><span class="name">Classic Omelet</span><span>$17.50</span></div><p class="item-desc">Ham, tomato, spinach, onion &amp; cheese omelet topped with fried cherry tomatoes &amp; turkish toast</p></div>
  <div class="item" style="left:75px;top:352px"><div class="item-head"><span class="name">Breaky Wrap</span><span>$15.00</span></div><p class="item-desc">Bacon, eggs, hash browns, cheese &amp; BBQ sauce on a toasted wrap</p></div>
  <div class="item" style="left:75px;top:412px"><div class="item-head"><span class="name">Breakfast Share Plate</span><span>$28.50</span></div><p class="item-desc">Bacon, sausages, hash browns, tomato, baked beans &amp; mushrooms with a slice of toasted pane bread &amp; your choice of fried, poached or scrambled eggs</p></div>
  <div class="item" style="left:75px;top:500px"><div class="item-head"><span class="name">Bacon Avocado Salsa</span><span>$17.50</span></div><p class="item-desc">Smashed avocado mixed with diced tomato &amp; bacon with spinach, a sprinkle of feta, a side of hash browns &amp; a wedge of lemon</p></div>

  <div class="item" style="left:448px;top:140px"><div class="item-head"><span class="name">Classic Breakfast</span><span>$16.50</span></div><p class="item-desc">Your choice of fried poached or scrambled eggs served with either bacon or sausages, tomato &amp; a slice of pane bread</p></div>
  <div class="item" style="left:448px;top:225px"><div class="item-head"><span class="name">Eggs Benedict</span><span>$19.00</span></div><p class="item-desc">Your choice of bacon, ham or salmon served with toasted turkish bread, poached eggs &amp; creamy hollandaise sauce</p></div>
  <div class="item" style="left:448px;top:290px"><div class="item-head"><span class="name">Panini Scramble</span><span>$16.50</span></div><p class="item-desc">Toasted panini bread topped with scrambled eggs, sauteed mushrooms, cherry tomatoes &amp; spinach with a drizzle of hollandaise sauce on top</p></div>
  <div class="item" style="left:448px;top:364px"><div class="item-head"><span class="name">Ultimate Breakfast Toastie</span><span>$16.50</span></div><p class="item-desc">Your choice of bacon, ham or salmon served with toasted turkish bread, poached eggs &amp; creamy hollandaise sauce</p></div>
  <div class="item" style="left:448px;top:432px"><div class="item-head"><span class="name">Fruity Pancakes</span><span>$17.50</span></div><p class="item-desc">2 fluffy pancakes topped with a tropical fruit mix including strawberries, mango &amp; blueberries with a sprinkle of icing sugar, served with maple syrup</p></div>

  <div class="brush" style="left:290px;top:628px;width:280px;height:26px"></div>
  <h2 class="section-title" style="top:585px">Lunch Menu</h2>

  <div class="item" style="left:75px;top:672px"><div class="item-head"><span class="name">Parmi Turkish Roll</span><span>$16.50</span></div><p class="item-desc">Chicken tenders, tomato relish, cheese, lettuce &amp; herb mayo served on a toasted turkish roll with a side of chips</p></div>
  <div class="item" style="left:75px;top:752px"><div class="item-head"><span class="name">Chicken Avocado Panini Roll</span><span>$15.50</span></div><p class="item-desc">Chicken, avocado, cheese &amp; aioli served on toasted panini bread &amp; grilled with a side of chips</p></div>
  <div class="item" style="left:75px;top:830px"><div class="item-head"><span class="name">Club Sandwich</span><span>$16.50</span></div><p class="item-desc">Three slices of toasted bread with ham, bacon, chicken, tomato, cheese, lettuce &amp; mayonnaise with a side of chips</p></div>
  <div class="item" style="left:75px;top:905px"><div class="item-head"><span class="name">Fish, Chips &amp; Salad</span><span>$15.00</span></div><p class="item-desc">Battered fillet with chips &amp; salad, herb mayonnaise, lemon &amp; salad dressing</p></div>

  <div class="item" style="left:448px;top:672px"><div class="item-head"><span class="name">Sweet Potato Chips</span><span>$13.50</span></div><p class="item-desc">Seasoned sweet potato chips served with a herb mayonnaise</p></div>
  <div class="item" style="left:448px;top:752px"><div class="item-head"><span class="name">Steak Sandwich</span><span>$17.50</span></div><p class="item-desc">Fillet steak with salad, cheese &amp; BBQ sauce on toasted bread with a side of chips</p></div>
  <div class="item" style="left:448px;top:822px"><div class="item-head"><span class="name">Fresh or Toasted Sandwich</span><span>$8.00</span></div><p class="item-desc">Your choice of meat, salad &amp; sauce on fresh white or wholemeal bread toasted or fresh</p></div>
  <div class="item" style="left:448px;top:900px"><div class="item-head"><span class="name">Nachos</span><span>$16.50</span></div><p class="item-desc">Nacho chips topped with nacho sauce, cheese sauce, melted cheese, sliced tomato &amp; smashed avocado</p></div>

</main>
</body>
</html>
```